interior designer/stylist looking for a letter press business card to reflect the stylish work

Hello Designers,
I need a business card design for an company called Halvern Interior Design. I'm aiming at the high end residential and private client market in London providing sleek simple interiors. I'd like my business card to be snipboard worthy and expensive looking, i want people to pin it and for it to have a sought after look, and want prospective customers to hire me as their interior designer as my card is so beautiful.
I love letter press design. I also like the use of colour/foil on the edge.
Colour combos & general things I like -
Black and White
Navy Blue and Gold
Neutral colours (muted palette of greys whites navys beiges)
White Marble & brass
Vaubris (fashion designer)
....also open to other suggestions....
Please dont take the pink in the attached photos too literally. i'd like the card to look more masculine than feminine.
I'd like Halvern on one side in one font, with interior design underneath so one word will make the statement....... unless anyone has any other ideas, open to suggestions.
I'd like a really simple font and for the whole card to look very graphic.
my details -
Maren Oakcliffe
Interior Designer & Stylist
email maren@halverninteriordesign.co.uk
phone +447813550296
website wwww.halverninteriordesign.co.uk
GO GO GO!! EXCITED TO SEE THE OUTCOME!!
x M
Target Market(s)
High End Residential and private clients
Industry/Entity Type
Business
Contact Information for Business Card
Halvern Interior Design & Styling
Maren Oakcliffe
phone +447813550296

```html
<!DOCTYPE html>
<html lang="en">
<head>
<meta charset="utf-8">
<title>Halvern Interior Design &amp; Styling — Business Card</title>
<link rel="stylesheet" href="https://fonts.googleapis.com/css2?family=Open+Sans:wght@400;700&display=swap">
<style>
  :root {
    --backdrop: #5c5c5c;
    --card: #fbfbf9;
    --edge-foil: #c9ab5c;
    --ink-bronze: #9b5a12;
  }
  * { margin: 0; padding: 0; box-sizing: border-box; }
  html, body {
    width: 1200px;
    height: 828px;
    overflow: hidden;
    background: var(--backdrop);
  }
  .stage {
    width: 1200px;
    height: 828px;
    display: flex;
    align-items: center;
    justify-content: center;
  }
  .business-card {
    width: 840px;
    height: 480px;
    background: var(--card);
    border: 4px solid var(--edge-foil);
    display: flex;
    flex-direction: column;
    align-items: center;
    justify-content: center;
    color: var(--ink-bronze);
    text-align: center;
    font-family: "Open Sans", sans-serif;
  }
  .business-name {
    font-weight: 400;
    font-size: 36px;
    line-height: 1.2;
  }
  .contact-block {
    margin-top: 30px;
    font-weight: 400;
    font-size: 22px;
    line-height: 1.3;
  }
  .contact-name {
    font-weight: 700;
    font-size: 27px;
  }
  .contact-role { margin-bottom: 12px; }
</style>
</head>
<body>
  <main class="stage">
    <section class="business-card">
      <h1 class="business-name">Halvern Interior Design &amp; Styling</h1>
      <div class="contact-block">
        <p class="contact-name">Maren Oakcliffe</p>
        <p class="contact-role">Interior Designer &amp; Stylist</p>
        <p class="contact-phone">+447813550296</p>
        <p class="contact-email">maren@halverninteriordesign.co.uk</p>
        <p class="contact-web">www.halverninteriordesign.co.uk</p>
      </div>
    </section>
  </main>
</body>
</html>
```